My Web Development Portfolio site

I'm a web developer and I need a web design that can showcase my web development portfolio. I like most of the websites from this link: http://www.pixelmarrow.com/portfolios/examples-594821. My ideal design should be modern, clean and fun. I will let the designer decided the color theme for the website.

Target Market(s)

Potential Employers.

Number of Pages Required

1 page

Requirements
Must have
• - Menu bar that includes at least: About Me, Blog, Contact, Project/Work
• - Excellent color theme
• - Use the logo I provided (see attachment)
Nice to have
• - Some animation
• - Fun yet modern design

```html
<!DOCTYPE html>
<html lang="en">
<head>
<meta charset="utf-8">
<title>Pathforge – Lorem Ipsum, User Experience Web Developer</title>
<link rel="stylesheet" href="https://fonts.googleapis.com/css2?family=Comfortaa:wght@400;600;700&family=Sansita:ital,wght@1,800&display=swap">
<style>
:root{
  --navy:#44546c;
  --navy-deep:#34425a;
  --orange:#f26b2a;
  --band:#efefef;
  --text:#4a4f58;
  --muted:#9aa0a8;
  --line:#e2e2e2;
  --white:#ffffff;
}
*{box-sizing:border-box;margin:0;padding:0}
html,body{width:1200px;height:3991px;overflow:hidden}
body{position:relative;background:var(--white);font-family:"Comfortaa",sans-serif;color:var(--text)}
.abs{position:absolute}
.bg-shapes{position:absolute;left:0;top:0;width:1200px;height:3991px}

/* header */
.brand{left:155px;top:18px;width:180px;text-align:center;color:var(--white)}
.brand-dot{width:38px;height:38px;border-radius:50%;border:4px solid var(--white);margin:0 auto 6px}
.brand-name{font-size:26px;font-weight:400;letter-spacing:.5px}
.menu{left:612px;top:52px;display:flex;gap:22px;list-style:none;font-size:15px;color:var(--white)}
.menu li{padding:6px 14px;border-radius:14px}
.menu li.active{background:var(--orange)}
.hero-title{left:0;width:1200px;top:258px;text-align:center;font-family:"Sansita",sans-serif;font-style:italic;font-weight:800;font-size:46px;color:var(--white)}
.hero-sub{left:0;width:1200px;top:322px;text-align:center;font-size:20px;color:var(--white)}

.section-title{font-family:"Sansita",sans-serif;font-style:italic;font-weight:800;font-size:30px;color:var(--orange)}
.btn{display:inline-block;background:var(--orange);color:var(--white);font-size:14px;padding:9px 22px;border-radius:18px}

/* about */
.avatar{left:262px;top:598px;width:194px;height:284px;border-radius:90px 90px 20px 20px;background:linear-gradient(#f3f3f3,#e4e6ea)}
.about-title{left:567px;top:628px}
.about-text{left:567px;top:694px;width:475px;font-size:14px;line-height:20px}
.about-text p{margin-bottom:16px}
.about-btn{left:567px;top:858px}
.quote{left:0;width:1200px;top:1128px;text-align:center;font-size:30px;line-height:38px;color:var(--navy)}
.quote em{font-family:"Sansita",sans-serif;font-style:italic;font-weight:800;color:var(--orange)}

/* work */
.work-title{left:0;width:1200px;top:1418px;text-align:center}
.filters{left:365px;top:1474px;width:678px;border-bottom:1px solid var(--line);display:flex;justify-content:center;gap:34px;font-size:13px;color:var(--muted);padding-bottom:8px}
.filters .on{color:var(--text)}
.tile{width:280px;overflow:hidden}
.tile-tag{position:absolute;left:0;top:18px;background:var(--white);color:var(--text);font-size:14px;padding:5px 22px 5px 14px;clip-path:polygon(0 0,100% 0,88% 50%,100% 100%,0 100%)}
.tile-over{background:rgba(30,30,35,.9);color:var(--white);text-align:center;padding-top:88px;font-size:17px;line-height:24px}
.tile-over .ttl{font-size:20px;margin-bottom:6px}
.tile-over .view{display:inline-block;margin-top:14px;border:2px solid var(--white);border-radius:16px;padding:5px 16px;font-size:15px}
.see-all{left:0;width:1200px;top:2393px;text-align:center}

.orange-text{left:0;width:1200px;top:2660px;text-align:center;font-size:28px;line-height:34px;color:var(--white)}

/* blog */
.blog-title{left:0;width:1200px;top:2954px;text-align:center}
.post{top:3018px;width:431px;height:473px;border:1px solid var(--line);background:var(--white)}
.post-img{width:100%;height:237px}
.post-body{padding:22px 26px}
.post-head{font-size:15px;line-height:20px;color:var(--navy)}
.post-meta{font-size:12px;color:var(--muted);margin:16px 0;display:flex;gap:24px}
.post-text{font-size:14px;line-height:19px}
.post-foot{position:absolute;left:26px;right:26px;bottom:22px;display:flex;justify-content:space-between;font-size:11px;color:var(--muted)}
.blog-all{left:0;width:1200px;top:3522px;text-align:center}

/* footer */
.foot-brand{left:155px;top:3708px;width:200px;text-align:center;color:var(--white)}
.foot-brand .brand-dot{width:46px;height:46px}
.foot-brand .brand-name{font-size:30px}
.contact-label{font-size:14px;color:var(--white)}
.contact-value{font-size:19px;color:var(--white);margin-top:4px}
.socials{left:766px;top:3862px;display:flex;gap:9px}
.socials span{width:24px;height:24px;border-radius:50%;background:#7d8aa0}
.copyright{left:155px;top:3958px;font-size:12px;color:var(--navy)}
</style>
</head>
<body>

<svg class="bg-shapes" viewBox="0 0 1200 3991" aria-hidden="true">
  <polygon points="0,890 1200,1078 1200,1424 0,1250" fill="var(--band)"/>
  <polygon points="0,2580 1200,2427 1200,2728 0,2960" fill="var(--orange)"/>
  <polygon points="0,3552 1200,3780 1200,3935 0,3935" fill="var(--navy)"/>
</svg>

<div class="abs" role="img" aria-label="Workspace photo of a desk with a monitor and plant, tinted slate blue" style="left:0;top:0;width:1200px;height:560px;background:linear-gradient(160deg,#5d6c83,#44546c 60%,#3a475c);clip-path:polygon(0 0,100% 0,100% 100%,0 78.5%)"></div>

<header>
  <div class="abs brand"><div class="brand-dot"></div><div class="brand-name">Pathforge</div></div>
  <ul class="abs menu">
    <li class="active">Home</li><li>About</li><li>Project/Work</li><li>Blog</li><li>Contact</li>
  </ul>
  <h1 class="abs hero-title">Hi, I’m Lorem Ipsum</h1>
  <p class="abs hero-sub">User Experience Web Developer</p>
</header>

<section>
  <div class="abs avatar" role="img" aria-label="Line illustration of the developer with glasses and a beard"></div>
  <h2 class="abs section-title about-title">About Me</h2>
  <div class="abs about-text">
    <p>Lorem ipsum dolor sit amet, consectetur adipiscing elit, sed do eiusmod tempor incididunt ut labore et dolore magna aliqua. Ut enim ad minim veniam, quis nostrud exercitation ullamco laboris nisi ut aliquip ex ea commodo consequat.</p>
    <p>Lorem ipsum dolor sit amet, consectetur adipiscing elit, sed do eiusmod tempor incididunt ut labore et.</p>
  </div>
  <span class="abs btn about-btn">Read More</span>
  <p class="abs quote">Lorem ipsum dolor sit <em>amet, consectetur</em> adipiscing<br>elit, sed do eiusmod tempor incididunt.</p>
</section>

<section>
  <h2 class="abs section-title work-title">Project / Work</h2>
  <div class="abs filters"><span class="on">ALL PROJECT</span><span>•</span><span>RESEARCH</span><span>•</span><span>WEB DESIGN</span><span>•</span><span>DEVELOPMENT</span></div>

  <div class="abs tile tile-over" style="left:154px;top:1538px;height:287px" role="img" aria-label="Project thumbnail with hover overlay">
    <div class="ttl">Lorem Ipsum</div>Lorem Ipsum is simply dummy<br>text of the printing<br><span class="view">View Project</span>
  </div>
  <div class="abs tile" style="left:154px;top:1849px;height:203px;background:linear-gradient(#6e7278,#2e3034)" role="img" aria-label="Vinyl sticker artwork"><span class="tile-tag">Vinyl Stickers</span></div>
  <div class="abs tile" style="left:154px;top:2075px;height:288px;background:linear-gradient(#9cc3e0,#5f9bc8)" role="img" aria-label="Web page design screenshot"><span class="tile-tag">Fabric Web</span></div>

  <div class="abs tile" style="left:460px;top:1538px;height:200px;background:linear-gradient(#2f5560,#8bb3b0)" role="img" aria-label="Vinyl sticker website mockup"><span class="tile-tag">Vinyl Stickers</span></div>
  <div class="abs tile" style="left:460px;top:1762px;height:375px;background:linear-gradient(#e6e8e8,#c9cccc)" role="img" aria-label="Photo of a green handbag on a chair"><span class="tile-tag">Wall Murals</span></div>
  <div class="abs tile" style="left:460px;top:2161px;height:202px;background:linear-gradient(#d8dcdc,#9fa6a6)" role="img" aria-label="Banner artwork of a green figure"><span class="tile-tag">Banners</span></div>

  <div class="abs tile" style="left:764px;top:1538px;height:287px;background:linear-gradient(#3d4a66,#e9ecf0 45%)" role="img" aria-label="Wall mural website screenshot"><span class="tile-tag">Wall Murals</span></div>
  <div class="abs tile" style="left:764px;top:1849px;height:203px;background:linear-gradient(#8ab9d8,#dfe9ef)" role="img" aria-label="Web page with hot air balloons"><span class="tile-tag">Fabric Web</span></div>
  <div class="abs tile" style="left:764px;top:2075px;height:288px;background:linear-gradient(#2f6aa0,#dde6ee)" role="img" aria-label="Company website screenshot"><span class="tile-tag">Wall Murals</span></div>

  <div class="abs see-all"><span class="btn">See All Work</span></div>
</section>

<p class="abs orange-text">Full of illustrations, sketches, cooking, coding, and<br>other happyramblings.</p>

<section>
  <h2 class="abs section-title blog-title">Welcome to my Blog</h2>
  <article class="abs post" style="left:154px">
    <div class="post-img" role="img" aria-label="Photo of hands typing on a laptop on a wooden desk" style="background:linear-gradient(135deg,#c98a4e,#8a5a34)"></div>
    <div class="post-body">
      <h3 class="post-head">Lorem Ipsum has been the industry's standard dummy text ever</h3>
      <div class="post-meta"><span>▢ Dec 4, 2016</span><span>○ Mira Castell</span></div>
      <p class="post-text">It is a long established fact that a reader will be distracted by the readable content of a page when looking at its layout. The point of using</p>
    </div>
    <div class="post-foot"><span>READ MORE →</span><span>♡ 05 / ▭ 04</span></div>
  </article>
  <article class="abs post" style="left:612px">
    <div class="post-img" role="img" aria-label="Photo of a developer looking at code on a monitor" style="background:linear-gradient(135deg,#3b4048,#6b6f74)"></div>
    <div class="post-body">
      <h3 class="post-head">Lorem Ipsum has been the industry's standard dummy text ever</h3>
      <div class="post-meta"><span>▢ Dec 4, 2016</span><span>○ Mira Castell</span></div>
      <p class="post-text">It is a long established fact that a reader will be distracted by the readable content of a page when looking at its layout. The point of using</p>
    </div>
    <div class="post-foot"><span>READ MORE →</span><span>♡ 05 / ▭ 04</span></div>
  </article>
  <div class="abs blog-all"><span class="btn">View All Blog</span></div>
</section>

<footer>
  <div class="abs foot-brand"><div class="brand-dot"></div><div class="brand-name">Pathforge</div></div>
  <div class="abs" style="left:155px;top:3842px"><div class="contact-label">Phone:</div><div class="contact-value">+1 (555) 014 2277</div></div>
  <div class="abs" style="left:458px;top:3842px"><div class="contact-label">Email:</div><div class="contact-value">hello@pathforge.dev</div></div>
  <div class="abs socials" aria-label="Social links"><span></span><span></span><span></span><span></span><span></span><span></span><span></span></div>
  <svg class="abs" style="left:1122px;top:3860px" width="20" height="26" viewBox="0 0 20 26" aria-label="Back to top"><path d="M10 24V3M3 10l7-7 7 7" stroke="#fff" stroke-width="3" fill="none"/></svg>
  <p class="abs copyright">©2016 Pathforge. All rights reserved.</p>
</footer>

</body>
</html>
```